Logo and metal business card design

Updated added my current logo which focus needs to be concentrated on. Have to have the new logo before the card. Company name is The Calder Works, LLC

Update: Reminder this is a Logo and business card design. I want the logo to be “CalderW” in a unique professional design that says secure, insurance, financial.

The G needs to be a P in the cut out

Update: the top two images have design on the metal which I am looking for

New black metal business cards. And CalderW.com logo that will go on the card. This will be a cut out design in the metal. Featuring “CalderW.com as the main cutout. Like the idea of .com to be separate or smaller and possible color. Looking for unique CalderW font design and a surrounding design per the examples below. Calder and G need to be different and the G a specific designing the mesh like the attached with the V in the mesh. But card side ways.. so mesh on right side of card with a G and .com in lower corner or where it fits Also looking to add my main info on the back side of the card. Derek M. Cell Email@mailbox-example.net We are an commercial insurance broker specializing in program business.
Updates

Need more time not enough entry’s and they are all the same.. I’m suppose to get 75 plus and not 20 that are the exact same from artist??? Need more submissions to compare. I committed my money so I do not want a refund I want more submissions from different artist

Target Market(s)

Insurance for the Restaurant industry

Industry/Entity Type

Insurance Broker

Contact Information for Business Card

New black metal business cards. And CalderW.com logo that will go on the card. This will be a cut out design in the metal. Featuring “CalderW.com as the main cutout. Like the idea of .com to be separate or smaller and possible color. Looking for unique CalderW font design and a surrounding design per the examples below. Calder and G need to be different and the G a specific designing the mesh like the attached with the V in the mesh. But card side ways.. so mesh on right side of card with a G and .com in lower corner or where it fits
Also looking to add my main info on the back side of the card.
Derek M.
Cell
Email@mailbox-example.net

We are an commercial insurance broker specializing in program business.

Logo Text

CalderW.com

Font styles to use
Decorative
Script
Other font styles liked:

Requirements
Must have
• Must have Calder and G distinctively different
Nice to have
• On flat parts I want texture on top of card

```html
<!DOCTYPE html>
<html lang="en">
<head>
<meta charset="UTF-8">
<title>CalderW Metal Business Card</title>
<link rel="stylesheet" href="https://fonts.googleapis.com/css2?family=Arimo&family=Raleway:wght@400&display=swap">
<style>
  :root {
    --page: #ffffff;
    --metal: #000000;
    --mesh-light: #f4f4f4;
    --mesh-mid: #d6d6d6;
    --mesh-dark: #bdbdbd;
    --accent: #1e88e5;
    --ink-light: #ffffff;
    --label: #000000;
  }
  html, body {
    margin: 0;
    padding: 0;
    width: 1200px;
    height: 1200px;
    overflow: hidden;
    background: var(--page);
  }
  .canvas {
    position: relative;
    width: 1200px;
    height: 1200px;
  }
  .side-label {
    position: absolute;
    left: 0;
    width: 1200px;
    text-align: center;
    font-family: "Arimo", Arial, sans-serif;
    font-size: 29px;
    line-height: 34px;
    color: var(--label);
    margin: 0;
  }
  .side-label--front { top: 36px; }
  .side-label--back { top: 634px; }

  .card {
    position: absolute;
    left: 178px;
    width: 844px;
    height: 485px;
    box-sizing: border-box;
    border: 5px solid var(--metal);
    border-radius: 24px;
    overflow: hidden;
    background: var(--page);
  }
  .card--front { top: 77px; }
  .card--back { top: 675px; }

  .mesh {
    position: absolute;
    left: 0;
    right: 0;
    background:
      radial-gradient(ellipse at 50% 50%, var(--mesh-light) 0%, var(--mesh-mid) 70%, var(--mesh-dark) 100%);
  }
  .card__band {
    position: absolute;
    left: 0;
    right: 0;
    background: var(--metal);
  }

  /* front */
  .card--front .mesh--top { top: 0; height: 166px; }
  .card--front .card__band { top: 166px; height: 148px; }
  .card--front .mesh--bottom { top: 314px; bottom: 0; }

  .brand {
    position: absolute;
    inset: 0;
  }
  .brand__dot {
    position: absolute;
    left: 240px;
    top: 38px;
    width: 72px;
    height: 72px;
    border-radius: 50%;
    background: var(--accent);
  }
  .brand__divider {
    position: absolute;
    left: 352px;
    top: 32px;
    width: 2px;
    height: 82px;
    background: var(--ink-light);
  }
  .brand__name {
    position: absolute;
    left: 382px;
    top: 32px;
    margin: 0;
    font-family: "Raleway", Arial, sans-serif;
    font-weight: 400;
    font-size: 70px;
    line-height: 80px;
    color: var(--accent);
  }

  /* back */
  .card--back .mesh--top { top: 0; height: 165px; }
  .card--back .card__band { top: 165px; height: 148px; }
  .card--back .mesh--bottom { top: 313px; bottom: 0; }

  .contact__name {
    position: absolute;
    left: 0;
    right: 0;
    top: 12px;
    margin: 0;
    text-align: center;
    font-family: "Raleway", Arial, sans-serif;
    font-weight: 400;
    font-size: 72px;
    line-height: 84px;
    color: var(--accent);
  }
  .contact__line {
    position: absolute;
    top: 96px;
    margin: 0;
    font-family: "Raleway", Arial, sans-serif;
    font-size: 22px;
    line-height: 28px;
    color: var(--ink-light);
    white-space: nowrap;
  }
  .contact__line--phone { left: 127px; }
  .contact__line--email { left: 440px; }
</style>
</head>
<body>
<main class="canvas">
  <p class="side-label side-label--front">Front</p>
  <section class="card card--front">
    <div class="mesh mesh--top" role="img" aria-label="Hexagonal honeycomb mesh cut into the metal"></div>
    <div class="card__band">
      <div class="brand">
        <span class="brand__dot"></span>
        <span class="brand__divider"></span>
        <h1 class="brand__name">CalderW</h1>
      </div>
    </div>
    <div class="mesh mesh--bottom" role="img" aria-label="Hexagonal honeycomb mesh cut into the metal"></div>
  </section>

  <p class="side-label side-label--back">Back</p>
  <section class="card card--back">
    <div class="mesh mesh--top" role="img" aria-label="Hexagonal honeycomb mesh cut into the metal"></div>
    <div class="card__band">
      <h2 class="contact__name">Derek M</h2>
      <p class="contact__line contact__line--phone">Phone : 555.010.4417</p>
      <p class="contact__line contact__line--email">Email : Derek@calderW.com</p>
    </div>
    <div class="mesh mesh--bottom" role="img" aria-label="Hexagonal honeycomb mesh cut into the metal"></div>
  </section>
</main>
</body>
</html>
```